PPT Template for a company that develops software and intellectual property for use by accountants a

We are a boutique firm that develops specialised reporting applications, financial and non-financial reporting content, checklists and other intellectual property for use by business consultants and accounting firms in particular. The applications and content we are creating is strategically focussed and we are required to produce reports and presentations and our current templates are simply not sufficient.

Excel worksheets, graphs and other graphics are regularly embedded into the presentations
We have our logo in 4 colour palettes and will require the winning version to be provided in all 4 colours plus B&W. There is one single logo but the name “Harbor Ledger Pathfinders” is presented in 3 different styles for use depending on the space available etc.
Our clients will typically take our products and rebrand/co brand these (we require them to at least say that there product is “powered by Harbor Ledger Pathfinders” with the logo.
The templates you provide will be used to create marketing presentations, proposal presentations and our standard documents that clients will rebrand or cobrand under license.

A Powerpoint Document Slide Template

Cover page layout, back page, intermediate page heading, in colours and styles based on the logo, title styles, and an intermediate or chapter heading slide style. Many of our presentations contain slides with tables, diagrams, flowcharts and text, including simple lists of bullet points. As above, you will see in our style guide that we have four coloured logos – we would like one version in each. We recommend that we finalise the design using the maroon version and then this be used as the base for the other colour palettes.
Again, the cover should be bold and draw attention but remain professional.

We are looking for something that works in both 4:3 and 16:9 (or two templates please)

We like a clear professional and simple look.

Deliverable: PowerPoint template file (.potx extension) for PowerPoint 2007 with at least a “cover” layout, a “title and content” layout, and a simplified slide layout, as well as “back cover”. Please embed any fonts used.

Industry/Entity Type

Financial

```html
<!DOCTYPE html>
<html lang="en">
<head>
<meta charset="utf-8">
<title>Harbor Ledger Pathfinders – Slide Template Set</title>
<link href="https://fonts.googleapis.com/css2?family=Open+Sans:wght@400;600;700&display=swap" rel="stylesheet">
<style>
:root{
  --red:#b01e28;
  --red-light:#e23a44;
  --pink:#fbe3e5;
  --ink:#333;
  --grey:#777;
  --grey-light:#e9e9e9;
  --footer:#6f6f6f;
  --stage:#000;
}
*{box-sizing:border-box;margin:0;padding:0}
html,body{width:1198px;height:1200px;overflow:hidden;background:var(--stage)}
body{position:relative;font-family:"Open Sans",Arial,sans-serif;color:var(--ink)}
.slide{position:absolute;width:380px;height:286px;background:#fff;overflow:hidden}
.c1{left:11px}.c2{left:404px}.c3{left:797px}
.r1{top:9px}.r2{top:307px}.r3{top:605px}.r4{top:903px}
.abs{position:absolute}
.footer{position:absolute;left:0;right:0;bottom:0;height:10px;background:var(--footer);color:#fff;font-size:4.8px;display:flex;justify-content:space-between;align-items:center;padding:0 6px}
.slide-title{position:absolute;left:8px;top:9px;font-size:11px;font-weight:700;color:var(--red);letter-spacing:.1px}
.header-rule{position:absolute;left:0;right:0;top:33px;height:1px;background:#e4e4e4}
.brand{position:absolute;display:flex;align-items:center;gap:3px}
.brand-dot{border-radius:50%;background:var(--red);flex:none}
.brand-name{color:#3a3a3a;font-weight:600;line-height:1.05}
.brand.small{right:6px;top:7px}
.brand.small .brand-dot{width:13px;height:13px}
.brand.small .brand-name{font-size:5.5px}
.brand.large .brand-dot{width:32px;height:32px}
.brand.large .brand-name{font-size:12.5px}
.body-text{font-size:5.2px;line-height:1.55;color:#888}
.section-label{font-size:7px;font-weight:700;color:var(--red)}
.photo{position:absolute}
.cover-photo{left:0;top:0;width:380px;height:167px;background:linear-gradient(135deg,#d9d9d9 0%,#f4f4f4 45%,#bdbdbd 100%)}
.cover-rule{left:0;top:167px;width:380px;height:2px;background:var(--red)}
.cover-title{left:243px;top:205px;font-size:12px;font-weight:700;color:var(--red)}
.cover-sub{left:243px;top:222px;font-size:8px;color:var(--grey)}
.cover-date{left:243px;top:238px;font-size:5.5px;color:var(--red)}
.chev-cols{left:24px;top:155px;width:333px;display:grid;grid-template-columns:repeat(5,1fr);gap:8px}
.tag-row{position:absolute;left:0;width:380px;height:44px}
.tag-row svg{position:absolute;left:0;top:0}
.tag-copy{position:absolute;left:90px;top:2px;right:8px}
.tag-head{font-size:7px;font-weight:700;color:var(--red);margin-bottom:2px}
.tag-head span{color:#555}
.back-bg{left:0;top:0;width:380px;height:276px;background:linear-gradient(160deg,#cfcfcf 0%,#f3f3f3 40%,#fafafa 100%)}
.thanks{left:105px;top:100px;font-size:10.5px;font-weight:700;color:#111}
.thanks span{color:var(--red)}
.back-divider{left:200px;top:128px;width:1px;height:110px;background:#d0d0d0}
.contact{left:215px;font-size:5.8px;color:#555;display:flex;align-items:center;gap:6px}
.contact-icon{width:10px;height:10px;border-radius:50%;background:var(--red);display:flex;align-items:center;justify-content:center}
.col-card{position:absolute;top:100px;width:88px}
.col-head{background:var(--red);color:#fff;font-size:6.8px;font-weight:700;padding:4px 6px}
.col-body{background:var(--grey-light);margin-top:4px;padding:6px;height:92px}
.chapter-bg{left:0;top:0;width:380px;height:276px;background:linear-gradient(135deg,#9fb0c6 0%,#dde4ee 40%,#c4cfdd 100%)}
.chapter-copy{position:absolute;left:184px;top:76px;width:175px;font-size:6.2px;color:#fff;line-height:1.6}
.chapter-copy p{margin-bottom:9px}
.chapter-title{left:6px;top:135px;font-size:10.5px;font-weight:700;color:var(--red)}
.grid-table{position:absolute;left:34px;top:102px;width:320px;border-collapse:collapse;font-size:5.2px}
.grid-table th{background:var(--red);color:#fff;font-size:6.8px;font-weight:700;height:18px;text-align:left;padding-left:8px}
.grid-table td{height:19px;padding-left:8px;color:#333;border-bottom:2px solid #fff}
.grid-table tr:nth-child(odd) td{background:#ececec}
.grid-table tr:nth-child(even) td{background:var(--pink)}
.top-band{left:0;top:0;width:380px;height:26px;background:linear-gradient(90deg,#fff 0%,#f2f5f9 55%,#c8d6e8 85%,#eef2f7 100%)}
.band-rule{left:0;top:37px;width:380px;height:1px;background:var(--red)}
.director{position:absolute;top:96px;width:95px;text-align:center}
.director-icon{width:53px;height:53px;margin:0 auto;border-radius:50%;background:var(--red);color:#fff;font:italic 700 26px Georgia,serif;display:flex;align-items:center;justify-content:center;border:2px solid #fff;box-shadow:0 0 0 1px var(--red)}
.director-name{font-size:6.8px;font-weight:700;color:var(--red);margin:5px 0 6px}
.director-body{background:var(--grey-light);padding:6px;height:86px;text-align:left}
.chart-bg{left:0;top:0;width:380px;height:276px;background:radial-gradient(circle at 55% 35%,#fff 0%,#f4f4f4 60%,#e9e9e9 100%)}
.y-label{position:absolute;left:27px;font-size:4.8px;color:#555}
.x-label{position:absolute;top:232px;font-size:4.8px;color:#555}
.cycle-art{left:205px;top:72px;width:145px;height:145px;border-radius:50%;background:radial-gradient(circle,#e6e6e6 0%,#d0d0d0 30%,#b01e28 32%,#9a1a22 100%)}
.bars-art{left:240px;top:100px;width:115px;height:115px;background:linear-gradient(90deg,#2f8bcb 0%,#3a9ad8 45%,#f08a00 55%,#ffa814 100%);opacity:.85}
</style>
</head>
<body>

<section class="slide c1 r1">
  <div class="photo cover-photo" role="img" aria-label="Black and white photo of a hand writing with a pen on paper"></div>
  <div class="abs cover-rule"></div>
  <div class="brand large" style="left:32px;top:198px">
    <span class="brand-dot"></span>
    <span class="brand-name">Harbor<br>Ledger<br>Pathfinders</span>
  </div>
  <div class="abs cover-title">COMPANY PROFILE</div>
  <div class="abs cover-sub">Persentator Director Name</div>
  <div class="abs cover-date">Date : 19-10-2014</div>
  <div class="footer" style="height:6px"></div>
</section>

<section class="slide c2 r1">
  <div class="slide-title">COMPANY PROFILE</div>
  <div class="brand small"><span class="brand-dot"></span><span class="brand-name">Harbor<br>Ledger<br>Pathfinders</span></div>
  <div class="header-rule"></div>
  <div class="abs section-label" style="left:26px;top:73px">Business Profile Title Here</div>
  <svg class="abs" style="left:24px;top:93px" width="333" height="46" viewBox="0 0 333 46">
    <g fill="#b01e28">
      <polygon points="0,0 60,0 70,23 60,46 0,46"/>
      <polygon points="65,0 126,0 136,23 126,46 65,46 75,23"/>
      <polygon points="131,0 192,0 202,23 192,46 131,46 141,23"/>
      <polygon points="197,0 258,0 268,23 258,46 197,46 207,23"/>
      <polygon points="263,0 323,0 333,23 323,46 263,46 273,23"/>
    </g>
    <g fill="none" stroke="#fff" stroke-width="1.4">
      <g transform="translate(33,21)"><circle r="7"/><path d="M-3 9h6M-2 12h4"/></g>
      <g transform="translate(100,21)"><circle r="7"/><path d="M-3 9h6M-2 12h4"/></g>
      <g transform="translate(166,21)"><circle r="7"/><path d="M-3 9h6M-2 12h4"/></g>
      <g transform="translate(232,21)"><circle r="7"/><path d="M-3 9h6M-2 12h4"/></g>
      <g transform="translate(298,21)"><circle r="7"/><path d="M-3 9h6M-2 12h4"/></g>
    </g>
  </svg>
  <div class="abs chev-cols body-text">
    <p>Lorem ipsum dolor sit amet lorem ipsum dolor sit amet lorem ipsum dolor sit amet lorem ipsum dolor sit amet lorem ipsum</p>
    <p>Lorem ipsum dolor sit amet lorem ipsum dolor sit amet lorem ipsum dolor sit amet lorem ipsum dolor sit amet lorem ipsum</p>
    <p>Lorem ipsum dolor sit amet lorem ipsum dolor sit amet lorem ipsum dolor sit amet lorem ipsum dolor sit amet lorem ipsum</p>
    <p>Lorem ipsum dolor sit amet lorem ipsum dolor sit amet lorem ipsum dolor sit amet lorem ipsum dolor sit amet lorem ipsum</p>
    <p>Lorem ipsum dolor sit amet lorem ipsum dolor sit amet lorem ipsum dolor sit amet lorem ipsum dolor sit amet lorem ipsum</p>
  </div>
  <div class="footer"><span>Powered By : Harbor Ledger Pathfinders.</span><span>Copyrights@2014</span></div>
</section>

<section class="slide c3 r1">
  <div class="slide-title">COMPANY PROFILE</div>
  <div class="brand small"><span class="brand-dot"></span><span class="brand-name">Harbor<br>Ledger<br>Pathfinders</span></div>
  <div class="header-rule"></div>
  <div class="tag-row" style="top:48px">
    <svg width="82" height="42"><polygon points="0,0 70,0 80,21 70,42 0,42" fill="#b01e28"/><g fill="none" stroke="#fff" stroke-width="1.4" transform="translate(38,19)"><circle r="8"/><path d="M-3 10h6M-2 13h4"/></g></svg>
    <div class="tag-copy"><div class="tag-head">TEXT HEADING <span>HERE</span></div><p class="body-text">Lorem ipsum dolor sit amet lorem ipsum dolor sit amet lorem ipsum dolor sit amet lorem ipsum dolor sit amet lorem ipsum dolor sit amet lorem ipsum dolor sit amet lorem ipsum dolor sit amet lorem ipsum dolor</p></div>
  </div>
  <div class="tag-row" style="top:104px">
    <svg width="82" height="42"><polygon points="0,0 70,0 80,21 70,42 0,42" fill="#b01e28"/><polygon points="38,8 47,21 38,34 29,21" fill="#fff"/></svg>
    <div class="tag-copy"><div class="tag-head">TEXT HEADING <span>HERE</span></div><p class="body-text">Lorem ipsum dolor sit amet lorem ipsum dolor sit amet lorem ipsum dolor sit amet lorem ipsum dolor sit amet lorem ipsum dolor sit amet lorem ipsum dolor sit amet lorem ipsum dolor sit amet lorem ipsum dolor</p></div>
  </div>
  <div class="tag-row" style="top:160px">
    <svg width="82" height="42"><polygon points="0,0 70,0 80,21 70,42 0,42" fill="#b01e28"/><g fill="none" stroke="#fff" stroke-width="2.4"><circle cx="38" cy="21" r="10"/><path d="M31 14l14 14"/></g></svg>
    <div class="tag-copy"><div class="tag-head">TEXT HEADING <span>HERE</span></div><p class="body-text">Lorem ipsum dolor sit amet lorem ipsum dolor sit amet lorem ipsum dolor sit amet lorem ipsum dolor sit amet lorem ipsum dolor sit amet lorem ipsum dolor sit amet lorem ipsum dolor</p></div>
  </div>
  <div class="tag-row" style="top:216px">
    <svg width="82" height="42"><polygon points="0,0 70,0 80,21 70,42 0,42" fill="#b01e28"/><g fill="none" stroke="#fff" stroke-width="1.6"><circle cx="38" cy="21" r="8"/><circle cx="38" cy="21" r="2.5" fill="#fff"/><path d="M38 9v6M38 27v6M26 21h6M44 21h6"/></g></svg>
    <div class="tag-copy"><div class="tag-head">TEXT HEADING <span>HERE</span></div><p class="body-text">Lorem ipsum dolor sit amet lorem ipsum dolor sit amet lorem ipsum dolor sit amet lorem ipsum dolor sit amet lorem ipsum dolor sit amet lorem ipsum dolor sit amet lorem ipsum dolor</p></div>
  </div>
  <div class="footer"><span>Powered By : Harbor Ledger Pathfinders.</span><span>Copyrights@2014</span></div>
</section>

<section class="slide c1 r2">
  <div class="photo back-bg" role="img" aria-label="Soft black and white photo of a hand holding a pen"></div>
  <div class="abs thanks">THANKS FOR YOUR <span>VALUABLE TIMES</span></div>
  <div class="brand large" style="left:50px;top:168px">
    <span class="brand-dot"></span>
    <span class="brand-name">Harbor<br>Ledger<br>Pathfinders</span>
  </div>
  <div class="abs back-divider"></div>
  <div class="abs contact" style="top:142px;display:block;width:150px;line-height:1.6">Contact Details line here Contact Details line here, Contact Details line here</div>
  <div class="abs contact" style="top:175px">
    <span class="contact-icon"><svg width="6" height="6" viewBox="0 0 10 10"><path d="M2 1l2 2-1 1.5c1 1.5 2 2.5 3.5 3.5L8 6l2 2-1.5 2C5 9 1 5 0 1.5z" fill="#fff"/></svg></span>01 5550-201030
  </div>
  <div class="abs contact" style="top:193px">
    <span class="contact-icon"><svg width="6" height="5" viewBox="0 0 10 8"><rect x="0.5" y="0.5" width="9" height="7" fill="none" stroke="#fff"/><path d="M0.5 0.5l4.5 4 4.5-4" fill="none" stroke="#fff"/></svg></span>hello@harborledger.example
  </div>
  <div class="abs contact" style="top:211px">
    <span class="contact-icon"><svg width="6" height="6" viewBox="0 0 10 10"><circle cx="5" cy="5" r="4.3" fill="none" stroke="#fff"/><path d="M0.7 5h8.6M5 0.7v8.6" stroke="#fff" stroke-width=".8"/></svg></span>www.harborledgerpathfinders.example
  </div>
  <div class="footer"><span>Powered By : Harbor Ledger Pathfinders.</span><span>Copyrights@2014</span></div>
</section>

<section class="slide c2 r2">
  <div class="slide-title">COMPANY PROFILE</div>
  <div class="brand small"><span class="brand-dot"></span><span class="brand-name">Harbor<br>Ledger<br>Pathfinders</span></div>
  <div class="header-rule"></div>
  <div class="abs section-label" style="left:33px;top:53px">Table Head Here</div>
  <p class="abs body-text" style="left:33px;top:64px;width:315px">Lorem ipsum dolor sit amet lorem ipsum dolor sit amet lorem ipsum dolor sit amet lorem ipsum dolor sit amet lorem ipsum dolor sit amet lorem ipsum dolor sit amet lorem ipsum dolor sit amet lorem ipsum dolor sit amet lorem ipsum dolor sit amet</p>
  <div class="col-card" style="left:35px"><div class="col-head">COL HEAD HERE</div><div class="col-body body-text">Lorem ipsum dolor sit amet lorem ipsum dolor sit amet lorem ipsum dolor sit amet lorem ipsum dolor sit amet lorem ipsum dolor sit amet lorem ipsum dolor sit amet lorem ipsum</div></div>
  <div class="col-card" style="left:140px"><div class="col-head">COL HEAD HERE</div><div class="col-body body-text">Lorem ipsum dolor sit amet lorem ipsum dolor sit amet lorem ipsum dolor sit amet lorem ipsum dolor sit amet lorem ipsum dolor sit amet lorem ipsum dolor sit amet lorem ipsum</div></div>
  <div class="col-card" style="left:245px"><div class="col-head">COL HEAD HERE</div><div class="col-body body-text">Lorem ipsum dolor sit amet lorem ipsum dolor sit amet lorem ipsum dolor sit amet lorem ipsum dolor sit amet lorem ipsum dolor sit amet lorem ipsum dolor sit amet lorem ipsum</div></div>
  <div class="footer"><span>Powered By : Harbor Ledger Pathfinders.</span><span>Copyrights@2014</span></div>
</section>

<section class="slide c3 r2">
  <div class="photo chapter-bg" role="img" aria-label="Blue tinted photo of a bright office with a chair"></div>
  <svg class="abs" style="left:128px;top:48px" width="252" height="180"><polygon points="32,0 252,0 252,180 32,180 0,90" fill="#b01e28" opacity=".92"/></svg>
  <div class="brand" style="left:20px;top:96px"><span class="brand-dot" style="width:22px;height:22px"></span><span class="brand-name" style="font-size:8px">Harbor<br>Ledger<br>Pathfinders</span></div>
  <div class="abs chapter-title">COMPANY PROFILE</div>
  <div class="chapter-copy">
    <p>Lorem ipsum dolor sit amet lorem ipsum dolor sit amet lorem ipsum dolor sit amet lorem ipsum dolor sit amet.</p>
    <p>Lorem ipsum dolor sit amet lorem ipsum dolor sit amet lorem ipsum.</p>
    <p>Lorem ipsum dolor sit amet lorem ipsum dolor sit amet lorem ipsum dolor sit amet lorem ipsum dolor sit amet.</p>
    <p>Lorem ipsum dolor sit amet lorem ipsum dolor sit amet lorem ipsum.</p>
  </div>
  <div class="footer"><span>Powered By : Harbor Ledger Pathfinders.</span><span>Copyrights@2014</span></div>
</section>

<section class="slide c1 r3">
  <div class="slide-title">COMPANY PROFILE</div>
  <div class="brand small"><span class="brand-dot"></span><span class="brand-name">Harbor<br>Ledger<br>Pathfinders</span></div>
  <div class="header-rule"></div>
  <div class="abs section-label" style="left:24px;top:97px;font-size:7.5px">Process Graph Text here</div>
  <p class="abs body-text" style="left:24px;top:112px;width:118px">Lorem ipsum dolor sit amet lorem ipsum dolor sit amet lorem ipsum dolor sit amet lorem ipsum dolor sit amet lorem ipsum dolor sit amet lorem ipsum dolor sit amet lorem ipsum dolor sit amet lorem ipsum dolor sit amet lorem ipsum dolor sit amet</p>
  <div class="photo cycle-art" role="img" aria-label="Four-step cycle diagram illustration in red and grey"></div>
  <div class="footer"><span>Powered By : Harbor Ledger Pathfinders.</span><span>Copyrights@2014</span></div>
</section>

<section class="slide c2 r3">
  <div class="slide-title">COMPANY PROFILE</div>
  <div class="brand small"><span class="brand-dot"></span><span class="brand-name">Harbor<br>Ledger<br>Pathfinders</span></div>
  <div class="header-rule"></div>
  <div class="abs section-label" style="left:33px;top:53px">Table Head Here</div>
  <p class="abs body-text" style="left:33px;top:64px;width:315px">Lorem ipsum dolor sit amet lorem ipsum dolor sit amet lorem ipsum dolor sit amet lorem ipsum dolor sit amet lorem ipsum dolor sit amet lorem ipsum dolor sit amet lorem ipsum dolor sit amet lorem ipsum dolor sit amet lorem ipsum dolor sit amet lorem ipsum dolor sit amet</p>
  <table class="grid-table">
    <thead><tr><th>TABLE HEAD HERE</th><th>TABLE HEAD HERE</th><th>TABLE HEAD HERE</th></tr></thead>
    <tbody>
      <tr><td>Subtext here Subtext here</td><td>Subtext here Subtext here</td><td>Subtext here Subtext here</td></tr>
      <tr><td>Subtext here Subtext here</td><td>Subtext here Subtext here</td><td>Subtext here Subtext here</td></tr>
      <tr><td>Subtext here Subtext here</td><td>Subtext here Subtext here</td><td>Subtext here Subtext here</td></tr>
      <tr><td>Subtext here Subtext here</td><td>Subtext here Subtext here</td><td>Subtext here Subtext here</td></tr>
      <tr><td>Subtext here Subtext here</td><td>Subtext here Subtext here</td><td>Subtext here Subtext here</td></tr>
      <tr><td>Subtext here Subtext here</td><td>Subtext here Subtext here</td><td>Subtext here Subtext here</td></tr>
    </tbody>
  </table>
  <div class="footer"><span>Powered By : Harbor Ledger Pathfinders.</span><span>Copyrights@2014</span></div>
</section>

<section class="slide c3 r3">
  <div class="photo top-band" role="img" aria-label="Faint blue photo strip of a pen on paper"></div>
  <div class="slide-title">COMPANY PROFILE</div>
  <div class="brand small"><span class="brand-dot"></span><span class="brand-name">Harbor<br>Ledger<br>Pathfinders</span></div>
  <div class="abs band-rule"></div>
  <div class="abs" style="left:24px;top:95px;font-size:10px;font-weight:700;color:#b01e28">Graph <span style="color:#333">Title Here</span></div>
  <p class="abs body-text" style="left:24px;top:113px;width:160px;font-size:5.6px;color:#777">Maecenas eget turpis lorem. Nunc vel metus augue. Aenean euismod cursus ligula eget dapibus. Praesent vel erat in tortor placerat dignissim. Duis dapibus aliquam mi, eget euismod sem scelerisque ut.<br><br>Vivamus at elit quis urna adipiscing iaculis. Curabitur vitae velit in neque dictum blandit. Proin in iaculis neque. Pellentesque habitant morbi tristique senectus et netus et malesuada fames ac turpis egestas.</p>
  <div class="photo bars-art" role="img" aria-label="Colourful growth graph illustration in blue and orange"></div>
  <div class="footer"><span>Powered By : Harbor Ledger Pathfinders.</span><span>Copyrights@2014</span></div>
</section>

<section class="slide c1 r4">
  <div class="photo top-band" role="img" aria-label="Faint blue photo strip of a pen on paper"></div>
  <div class="slide-title">COMPANY PROFILE</div>
  <div class="brand small"><span class="brand-dot"></span><span class="brand-name">Harbor<br>Ledger<br>Pathfinders</span></div>
  <div class="abs band-rule"></div>
  <div class="footer"><span>Powered By : Harbor Ledger Pathfinders.</span><span>Copyrights@2014</span></div>
</section>

<section class="slide c2 r4">
  <div class="slide-title">COMPANY PROFILE</div>
  <div class="brand small"><span class="brand-dot"></span><span class="brand-name">Harbor<br>Ledger<br>Pathfinders</span></div>
  <div class="header-rule"></div>
  <div class="abs section-label" style="left:33px;top:53px">Director Profile</div>
  <p class="abs body-text" style="left:33px;top:64px;width:315px">Lorem ipsum dolor sit amet lorem ipsum dolor sit amet lorem ipsum dolor sit amet lorem ipsum dolor sit amet lorem ipsum dolor sit amet lorem ipsum dolor sit amet lorem ipsum dolor sit amet lorem ipsum dolor sit amet</p>
  <div class="director" style="left:40px"><div class="director-icon">i</div><div class="director-name">DIRECTOR NAME</div><div class="director-body body-text">Lorem ipsum dolor sit amet lorem ipsum dolor sit amet lorem ipsum dolor sit amet lorem ipsum dolor sit amet lorem ipsum dolor sit amet lorem ipsum dolor sit</div></div>
  <div class="director" style="left:148px"><div class="director-icon">i</div><div class="director-name">DIRECTOR NAME</div><div class="director-body body-text">Lorem ipsum dolor sit amet lorem ipsum dolor sit amet lorem ipsum dolor sit amet lorem ipsum dolor sit amet lorem ipsum dolor sit amet lorem ipsum dolor sit</div></div>
  <div class="director" style="left:256px"><div class="director-icon">i</div><div class="director-name">DIRECTOR NAME</div><div class="director-body body-text">Lorem ipsum dolor sit amet lorem ipsum dolor sit amet lorem ipsum dolor sit amet lorem ipsum dolor sit amet lorem ipsum dolor sit amet lorem ipsum dolor sit</div></div>
  <div class="footer"><span>Powered By : Harbor Ledger Pathfinders.</span><span>Copyrights@2014</span></div>
</section>

<section class="slide c3 r4">
  <div class="photo chart-bg" role="img" aria-label="Soft grey textured background"></div>
  <div class="abs" style="left:10px;top:9px;font-size:11px;font-weight:700;color:#333">Project <span style="color:#b01e28">Title Here</span></div>
  <div class="brand small"><span class="brand-dot"></span><span class="brand-name">Harbor<br>Ledger<br>Pathfinders</span></div>
  <div class="header-rule"></div>
  <div class="abs" style="left:28px;top:64px;font-size:6.2px;color:#333">Lorem ipsum dolor sit ipsum Lorem ipsum dolor sit ipsum Lorem ipsum Lorem ipsum</div>
  <div class="y-label" style="top:92px">Lorem ipsum text here</div>
  <div class="y-label" style="top:118px">Lorem ipsum text here</div>
  <div class="y-label" style="top:144px">Lorem ipsum text here</div>
  <div class="y-label" style="top:170px">Lorem ipsum text here</div>
  <div class="y-label" style="top:196px">Lorem ipsum text here</div>
  <div class="y-label" style="top:222px">Lorem ipsum text here</div>
  <svg class="abs" style="left:85px;top:85px" width="255" height="145">
    <path d="M5 0V142H253" fill="none" stroke="#bbb" stroke-width=".8"/>
    <rect x="6" y="97" width="17" height="45" fill="#999"/>
    <rect x="23" y="61" width="19" height="81" fill="#b01e28"/>
    <rect x="48" y="75" width="19" height="67" fill="#e23a44"/>
    <rect x="72" y="103" width="19" height="39" fill="#b01e28"/>
    <rect x="97" y="131" width="19" height="11" fill="#e00000"/>
    <rect x="121" y="138" width="19" height="4" fill="#777"/>
    <rect x="147" y="15" width="19" height="127" fill="#b01e28"/>
    <rect x="172" y="130" width="19" height="12" fill="#b01e28"/>
    <rect x="196" y="135" width="19" height="7" fill="#e23a44"/>
  </svg>
  <div class="x-label" style="left:91px">Lorem ipsum text here</div>
  <div class="x-label" style="left:168px">Lorem ipsum text here</div>
  <div class="x-label" style="left:273px">Lorem ipsum text here</div>
  <div class="footer"><span>Powered By : Harbor Ledger Pathfinders.</span><span>Copyrights@2014</span></div>
</section>

</body>
</html>
```